Winery Needs a flyer for a dinner show with a tribute band/show

We will have a dinner and show with hosted beer and wine. The show will be a tribute to the Moon Crew. The event will be on November 1, 2019 from 6pm-10pm with dinner starting at 6:30pm. Would like to have on the flyer GTL DinnerGuild Presents... A tribute to the Moon Crew. Enjoy an evening with the Stars under the Stars on the HillPaths.... Club Members $159.00 General Public $189.00 tickets can be purchased online at www.HillPathCellars.example, call in 555.304.7712 or at the Sipping Hall, 4870 Marbrook Court Fairfield, Ca 90001. Included files as example and some of our logos. Just examples looking forward to your creativity.

Target Market(s)

Wine Drinkers, age 30-60, outdoor people

Font styles to use
Sans Serif
Other font styles liked:
• cottage and Barn

Colors

Designer to choose colors to be used in the design.

Requirements
Must have
• All important information to purchase tickets
Nice to have
• classic and reto if possible while still incorporating our logo somewhere

```html
<!DOCTYPE html>
<html lang="en">
<head>
<meta charset="utf-8">
<title>GTL DinnerGuild Presents – A Tribute to the Moon Crew</title>
<link rel="stylesheet" href="https://fonts.googleapis.com/css2?family=League+Gothic&display=swap">
<style>
  :root{
    --brown-deep:#2f1c15;
    --brown:#3b241b;
    --yellow:#f7d046;
    --orange:#f2902a;
    --ink:#3a2417;
    --white:#ffffff;
    --shadow:#1d110c;
  }
  *{margin:0;padding:0;box-sizing:border-box}
  html,body{width:848px;height:1200px;overflow:hidden;background:var(--brown)}
  .flyer{position:relative;width:848px;height:1200px;overflow:hidden;background:var(--brown);font-family:"League Gothic","Arial Narrow",sans-serif;text-transform:uppercase}
  .photo{position:absolute;left:0;top:0;width:848px;height:1200px;
    background:
      radial-gradient(ellipse 200px 230px at 410px 330px, rgba(220,205,185,.55), transparent 70%),
      radial-gradient(ellipse 170px 260px at 250px 360px, rgba(205,190,170,.35), transparent 70%),
      radial-gradient(ellipse 170px 260px at 590px 360px, rgba(205,190,170,.35), transparent 70%),
      linear-gradient(160deg, transparent 55%, rgba(201,179,154,.55) 78%, rgba(160,135,110,.35) 92%, transparent 100%),
      linear-gradient(180deg, #4a3226 0%, var(--brown) 60%, var(--brown-deep) 100%);}
  .logo-tab{position:absolute;left:342px;top:0;width:165px;height:165px;background:var(--white);
    clip-path:polygon(0 0,100% 0,100% 74%,50% 100%,0 74%);
    display:flex;flex-direction:column;align-items:center;justify-content:center;gap:6px;padding-bottom:30px}
  .logo-dot{width:22px;height:22px;border-radius:50%;background:var(--brown)}
  .logo-name{font-size:38px;letter-spacing:4px;color:var(--brown);line-height:1}
  .presents{position:absolute;left:151px;top:456px;width:550px;display:flex;align-items:center;gap:10px;color:var(--orange);font-size:42px;line-height:1;white-space:nowrap}
  .presents .rule{flex:1;height:6px;background:var(--orange);clip-path:polygon(0 50%,100% 0,100% 100%)}
  .presents .rule.right{clip-path:polygon(0 0,100% 50%,0 100%)}
  .title{position:absolute;left:0;width:848px;text-align:center;color:var(--yellow);line-height:1;text-shadow:5px 5px 0 var(--shadow);white-space:nowrap;display:block;font-weight:400}
  .title.line-one{top:496px;font-size:168px}
  .title.line-two{top:640px;font-size:160px}
  .ribbon{position:absolute;left:151px;top:808px;width:554px;height:80px;background:var(--yellow);
    clip-path:polygon(0 0,100% 0,95% 50%,100% 100%,0 100%,5% 50%);
    display:flex;flex-direction:column;align-items:center;justify-content:center;color:var(--ink);font-size:33px;line-height:.95}
  .ticket-icon{position:absolute;left:129px;top:909px;width:86px;height:86px}
  .price{position:absolute;top:906px;color:var(--yellow);font-size:96px;line-height:1;text-shadow:3px 3px 0 var(--shadow)}
  .price.member{left:222px}
  .price.public{left:367px}
  .price-label{position:absolute;top:1004px;color:var(--orange);font-size:22px;line-height:1}
  .price-label.member{left:230px}
  .price-label.public{left:374px}
  .online{position:absolute;left:491px;top:928px;width:230px;color:var(--orange);font-size:27px;line-height:.95}
  .online .url{font-size:22px}
  .address{position:absolute;left:0;top:1040px;width:848px;text-align:center;color:var(--orange);font-size:29px;line-height:1}
  .phone{position:absolute;left:0;top:1074px;width:848px;display:flex;justify-content:center;align-items:center;gap:12px}
  .phone svg{width:72px;height:70px}
  .phone-number{color:var(--yellow);font-size:100px;line-height:1;text-shadow:3px 3px 0 var(--shadow)}
</style>
</head>
<body>
<main class="flyer">
  <div class="photo" role="img" aria-label="Sepia stage photograph of three crooners in tuxedos singing together at a microphone, with a bar set-up behind them"></div>

  <div class="logo-tab">
    <span class="logo-dot"></span>
    <span class="logo-name">GTL</span>
  </div>

  <p class="presents"><span class="rule"></span>GTL DinnerGuild Presents<span class="rule right"></span></p>

  <h1>
    <span class="title line-one">A Tribute To</span>
    <span class="title line-two">The Moon Crew</span>
  </h1>

  <div class="ribbon">
    <span>Enjoy an evening with the stars</span>
    <span>under the stars on the HillPaths</span>
  </div>

  <svg class="ticket-icon" viewBox="0 0 86 86" fill="none" stroke="#f2902a" stroke-width="4" stroke-linejoin="round" aria-hidden="true">
    <path d="M22 38 L50 8 L72 28 L46 40"/>
    <path d="M30 30 L52 16 L62 26"/>
    <rect x="4" y="40" width="72" height="38" rx="4"/>
    <rect x="16" y="50" width="48" height="18"/>
    <path d="M22 59 h36" stroke-dasharray="4 4"/>
  </svg>

  <p class="price member">$159</p>
  <p class="price-label member">Club Members</p>
  <p class="price public">$189</p>
  <p class="price-label public">General Public</p>

  <p class="online">Tickets can be<br>purchased online at<br><span class="url">www.HillPathCellars.example</span></p>

  <p class="address">The Sipping Hall, 4870 Marbrook Court Fairfield, CA 90001</p>

  <div class="phone">
    <svg viewBox="0 0 80 78" aria-hidden="true">
      <path fill="#f7d046" d="M14 8c4-3 8-3 10 1l8 13c2 3 1 6-2 8l-5 4c3 9 11 18 21 22l4-5c2-3 5-4 8-2l13 8c4 2 4 6 1 10l-5 5c-5 5-15 4-28-4S10 45 5 32C1 22 3 16 8 12z"/>
      <path fill="none" stroke="#f7d046" stroke-width="5" stroke-linecap="round" d="M44 20a18 18 0 0 1 16 16M46 8a30 30 0 0 1 26 26"/>
    </svg>
    <span class="phone-number">555.304.7712</span>
  </div>
</main>
</body>
</html>
```